Business cards and stationery for dental surgery products company
Dental Crestline Works, LLC
Business cards and stationery for dental surgery products company - Medical
Creative Brief
Simple
Boris Kestrow
No address.
boris.kestrow@fernmail.example
Regenerative Products Surgical Supplies
Harbor Cell Providers - Quintara Ossel Vanta Spa, USA - Disposable Surgical Devices
bkestrow bkestrow
Designers - Thanks so much for all the concepts! The world is full of amazingly creative people! I apologize for not responding recently. The holidays go me behind at my work. Then my area of the US had a winter storm that knocked out my internet service for a couple of days. So, I have been playing catch up on my work and have failed to stay on top of this project. Here are a couple of items for everyone. My website will be - www.dentalcrestlineworks.example My Facebook info is - www.socialpage.example/dentalcrestlineworks. Also, this will be my primary online vehicle. I will use it to point to my manufacturer's sites, as well as update my doctors daily. I want to remind the new comers, this is for a total stationary packet. -business cards -note / thank you cards (no need for the actual words "Thank you") -note pads -letter head -fax cover sheet -folder -simple email signature -envelopes (both regular size and also 8.5" x 11" size for literature) I hope this helps. I will let the contest run its full length of time, then post my decision sometime Monday 1/13 CST. Thanks so much! Boris
Wow! Lots of design ideas very quickly. Please remember, I need more than business cards!!
Designers - For some reason my comments did not upload correctly. What you see on the brief was from an old project that was deleted. ***Please note the following items. >>> I need a complete stationary package - business cards, thank you cards (a MUST!), note pad, letter head, folders, etc. >>> I need the business cards in white. I would like the logo on the back, with possibly a "ghosted" version of the tooth on the logo, without the name on it, enlarged and on the back of the card as well. I do not need the comments about Harbor Cell or Vanta on the cards. Nor, do I need regenerative products or disposable surgical supplies on the card. >>> I need an editable version that I can add the website, facebook, and business email address to at a later date. >>> PLEASE CONTACT ME IF YOU HAVE ANY QUESTIONS. Thanks! Boris
I'm not sure how these two got separated. I want the logo first, then use it on the business cards and stationery. Sorry for any confusion.

```html
<!DOCTYPE html>
<html lang="en">
<head>
<meta charset="utf-8">
<title>Dental Crestline Works — Business Card</title>
<link rel="stylesheet" href="https://fonts.googleapis.com/css2?family=Arimo:wght@400;700&display=swap">
<style>
  :root {
    --backdrop: #e6e6e4;
    --card-white: #ffffff;
    --brand-blue: #1f86cf;
    --brand-blue-deep: #0f5fa6;
    --brand-blue-light: #58b4ea;
    --ink-grey: #5e6166;
    --soft-grey: #c9ccd1;
    --silver: #d7dbe0;
  }
  * { box-sizing: border-box; margin: 0; padding: 0; }
  html, body { width: 1200px; height: 600px; overflow: hidden; }
  body {
    background: var(--backdrop);
    font-family: "Arimo", Arial, sans-serif;
    position: relative;
  }
  .card {
    position: absolute;
    top: 157px;
    width: 500px;
    height: 286px;
    border-radius: 14px;
    overflow: hidden;
    box-shadow: 0 10px 24px rgba(0,0,0,0.22);
  }
  .card-front { left: 60px; background: var(--card-white); }
  .card-back  { left: 640px; background: var(--brand-blue); }

  .brand-mark {
    position: absolute;
    display: flex;
    align-items: center;
    gap: 8px;
  }
  .brand-dot {
    width: 26px; height: 26px;
    border-radius: 50%;
    background: var(--brand-blue);
    flex: none;
  }
  .brand-name {
    font-weight: 700;
    font-size: 22px;
    letter-spacing: -0.3px;
    color: var(--brand-blue-deep);
    white-space: nowrap;
  }
  .card-front .brand-mark { left: 26px; top: 34px; }

  .holder-name {
    position: absolute;
    left: 30px; top: 174px;
    font-size: 16px;
    color: var(--brand-blue);
  }
  .contact-list {
    position: absolute;
    left: 30px; top: 202px;
    list-style: none;
    font-size: 10px;
    color: var(--ink-grey);
    line-height: 16px;
  }
  .contact-list li { display: flex; align-items: center; gap: 6px; }
  .contact-list svg { width: 10px; height: 10px; fill: var(--brand-blue); }

  .social-handle {
    position: absolute;
    left: 206px; top: 204px;
    display: flex; align-items: center; gap: 6px;
    font-size: 10px;
    color: var(--ink-grey);
  }
  .social-square {
    width: 12px; height: 12px;
    background: var(--brand-blue);
    border-radius: 2px;
  }

  .footer-band {
    position: absolute;
    left: 0; bottom: 0;
    width: 500px; height: 70px;
  }
  .website {
    position: absolute;
    right: 22px; bottom: 11px;
    font-size: 9px;
    color: #ffffff;
    white-space: nowrap;
    z-index: 1;
  }

  .card-back .brand-mark {
    left: 12px; top: 262px;
    transform: rotate(-90deg);
    transform-origin: left top;
  }
  .card-back .brand-name { color: #ffffff; font-size: 21px; }
  .card-back .brand-dot { background: #ffffff; width: 22px; height: 22px; }

  .puzzle-art {
    position: absolute;
    right: 0; top: 0;
    width: 370px; height: 286px;
    background: linear-gradient(135deg, #eef0f3 0%, var(--silver) 45%, #a9b0b8 75%, var(--brand-blue-light) 100%);
    clip-path: polygon(22% 0, 100% 0, 100% 100%, 48% 100%, 30% 62%, 12% 30%);
  }
</style>
</head>
<body>
  <section class="card card-front" aria-label="Business card front">
    <div class="brand-mark">
      <span class="brand-dot"></span>
      <span class="brand-name">Dental Crestline Works</span>
    </div>

    <p class="holder-name">Boris Kestrow</p>
    <ul class="contact-list">
      <li>
        <svg viewBox="0 0 10 10" aria-hidden="true"><path d="M2 0h2l1 3-1.5 1a6 6 0 0 0 2.5 2.5L7 5l3 1v2l-1 2C4 10 0 6 0 1z"/></svg>
        555.010.4821
      </li>
      <li>
        <svg viewBox="0 0 10 10" aria-hidden="true"><path d="M0 2h10v6H0z"/></svg>
        boris.kestrow@fernmail.example
      </li>
    </ul>

    <div class="social-handle">
      <span class="social-square"></span>
      /dentalcrestlineworks
    </div>

    <svg class="footer-band" viewBox="0 0 500 70" preserveAspectRatio="none" aria-hidden="true">
      <path d="M0 62 C150 72 300 62 500 30 L500 70 L0 70 Z" fill="var(--soft-grey)"/>
      <path d="M150 64 C290 60 400 38 500 6 L500 52 C400 66 290 72 150 70 Z" fill="var(--brand-blue)"/>
    </svg>
    <p class="website">www.dentalcrestlineworks.example</p>
  </section>

  <section class="card card-back" aria-label="Business card back">
    <div class="puzzle-art" role="img" aria-label="Silver and blue interlocking puzzle pieces decoration"></div>
    <div class="brand-mark">
      <span class="brand-dot"></span>
      <span class="brand-name">Dental Crestline Works</span>
    </div>
  </section>
</body>
</html>
```